Redesign website

I purchased a business a few months ago and I'm in the process on rebranding everything and creating a new website. I want the new website completely different with 5 pages and nice pictures on every page. Also I want my new logo and colors to included on the site.
Current Site https://www.brindlehoundco.com

Industry/Entity Type

Dog Sitting

Coding

Coded - Design and coding required

Number of Pages Required

5+ page

Requirements
Must have
• I have pictures and a video I can shared to use for the website.
Just as the current site it should have an option to be taken to the site I have to make reservations.
Nice to have
• Would be nice to have social media intergrations

```html
<!DOCTYPE html>
<html lang="en">
<head>
<meta charset="utf-8">
<title>Brindle Hound Pet Boarding &amp; Daycare</title>
<link href="https://fonts.googleapis.com/css2?family=Montserrat:wght@400;500;600;700&family=Baloo+2:wght@700;800&family=Playfair+Display:wght@400&display=swap" rel="stylesheet">
<style>
:root{
  --teal:#4ab5a8;
  --teal-dark:#3fa396;
  --magenta:#c4127f;
  --ink:#2f2f2f;
  --text:#5a5a5a;
  --grey-bg:#f4f4f4;
  --footer:#3a3a3a;
  --white:#ffffff;
}
*{box-sizing:border-box;margin:0;padding:0}
html,body{width:1200px;height:3934px;overflow:hidden}
body{position:relative;background:var(--white);font-family:'Montserrat',sans-serif;color:var(--text)}
.abs{position:absolute}
.tear{position:absolute;left:0;width:1200px;height:22px;display:block}
.tear.flip{transform:scaleY(-1)}
.serif{font-family:'Playfair Display',serif;font-weight:400;color:var(--ink)}
.underline{position:absolute;height:4px;background:var(--magenta);border-radius:2px}
.btn{position:absolute;display:flex;align-items:center;justify-content:center;border-radius:30px;font-weight:600;font-size:14px;color:var(--white);background:var(--magenta);letter-spacing:.3px}

/* header */
.topbar-text{font-size:14px;color:var(--ink)}
.icon-dot{position:absolute;border-radius:50%;background:var(--magenta);display:flex;align-items:center;justify-content:center}
.social-dot{position:absolute;width:24px;height:24px;border-radius:50%;background:var(--teal)}
.nav a{position:absolute;top:57px;font-size:13px;font-weight:500;color:var(--ink);text-decoration:none}
.nav a.active{color:var(--magenta);font-weight:600}
.nav-line{position:absolute;left:0;top:82px;width:1200px;height:1px;background:#e2e2e2}
.brand-badge{position:absolute;left:513px;top:-12px;width:174px;height:174px;border-radius:50%;background:var(--white);box-shadow:0 2px 6px rgba(0,0,0,.15);display:flex;align-items:center;justify-content:center;z-index:5}
.brand-badge span{font-weight:700;font-size:22px;color:var(--magenta);text-align:center;line-height:1.1}

/* hero */
.hero-photo{position:absolute;left:0;top:83px;width:1200px;height:590px;background:radial-gradient(ellipse at 72% 55%,#e8d8bf 0%,#c9a97e 14%,transparent 30%),linear-gradient(180deg,#6f7a4a 0%,#8a8a55 35%,#a88d63 70%,#c7a77e 100%)}
.hero-welcome{left:162px;top:266px;font-size:24px;font-weight:500;color:var(--white)}
.hero-title{left:162px;top:298px;font-family:'Baloo 2',sans-serif;font-weight:800;font-size:52px;line-height:58px;color:var(--white)}

/* about */
.about-photo{position:absolute;left:163px;top:774px;width:416px;height:416px;border-radius:50%;border:3px solid var(--teal);background:linear-gradient(180deg,#4f8fe0 0%,#8fb9ef 38%,#eae2c8 52%,#b9b4a4 78%,#8d8a80 100%)}
.play{position:absolute;left:345px;top:956px;width:52px;height:52px;border-radius:50%;background:var(--white);display:flex;align-items:center;justify-content:center}
.about-title{left:600px;top:780px;font-size:54px}
.about-body{left:600px;top:858px;width:440px;font-size:12px;line-height:24px}
.about-body p+p{margin-top:12px}
.about-sign{left:601px;top:1154px;font-size:13px;font-weight:600;color:var(--magenta)}

/* services */
.services-band{position:absolute;left:0;top:1318px;width:1200px;height:325px;background:var(--teal)}
.services-title{left:0;width:1200px;top:1386px;text-align:center;font-size:54px;color:var(--white)}
.service-photo{position:absolute;width:242px;height:242px;border-radius:50%;border:4px solid var(--teal)}
.service-name{position:absolute;width:300px;text-align:center;font-size:25px;font-weight:600;color:var(--ink)}
.service-text{position:absolute;width:270px;text-align:center;font-size:12px;line-height:24px}

/* gallery */
.gallery-bg{position:absolute;left:0;top:2030px;width:1200px;height:888px;background:var(--grey-bg)}
.gallery-title{left:0;width:1200px;top:2096px;text-align:center;font-size:54px}
.tile{position:absolute;border-radius:4px}

/* contact */
.contact-title{left:0;width:1200px;top:2982px;text-align:center;font-size:54px}
.c-icon{position:absolute;left:183px;width:64px;height:64px;border-radius:50%;border:2px solid var(--teal);display:flex;align-items:center;justify-content:center}
.c-label{position:absolute;left:273px;font-size:20px;font-weight:600;color:var(--ink)}
.c-val{position:absolute;left:273px;font-size:13px;color:var(--ink);line-height:22px}
.form-box{position:absolute;left:600px;top:3102px;width:416px;height:387px;background:var(--teal);border-radius:4px}
.form-box h3{position:absolute;left:38px;top:34px;font-size:19px;font-weight:600;color:var(--white)}
.form-box .rule{position:absolute;left:38px;top:68px;width:46px;height:2px;background:var(--white)}
.field{position:absolute;left:37px;width:338px;background:var(--white);border-radius:3px;font-size:10px;font-weight:500;color:var(--ink);padding:12px 16px}

/* footer */
.footer{position:absolute;left:0;top:3580px;width:1200px;height:354px;background:var(--footer)}
.footer-brand{left:0;width:1200px;top:3680px;text-align:center;font-size:40px;font-weight:600;color:var(--white)}
.footer-line{position:absolute;left:0;width:1200px;height:1px;background:#5a5a5a}
.footer-nav a{position:absolute;top:3820px;font-size:12px;font-weight:500;color:var(--white);text-decoration:none}
.copy{left:161px;top:3893px;font-size:14px;color:var(--white)}
.f-social{position:absolute;top:3889px;width:28px;height:28px;border-radius:50%;border:1.5px solid var(--white)}
</style>
</head>
<body>

<svg width="0" height="0" style="position:absolute">
  <defs>
    <path id="torn" d="M0,12 L30,8 L55,13 L90,6 L120,11 L160,7 L195,14 L230,9 L270,12 L300,5 L340,10 L380,8 L410,13 L450,7 L490,11 L520,6 L560,12 L600,9 L640,13 L670,6 L710,10 L750,8 L790,14 L820,7 L860,11 L900,6 L940,12 L970,9 L1010,13 L1050,7 L1090,11 L1120,6 L1160,12 L1200,8 L1200,22 L0,22 Z"/>
  </defs>
</svg>

<!-- header -->
<header>
  <div class="icon-dot" style="left:162px;top:9px;width:24px;height:24px">
    <svg width="12" height="12" viewBox="0 0 24 24"><path fill="#fff" d="M6.6 10.8a15 15 0 0 0 6.6 6.6l2.2-2.2a1 1 0 0 1 1-.25 11.4 11.4 0 0 0 3.6.57 1 1 0 0 1 1 1V20a1 1 0 0 1-1 1A17 17 0 0 1 3 4a1 1 0 0 1 1-1h3.5a1 1 0 0 1 1 1c0 1.25.2 2.45.57 3.57a1 1 0 0 1-.25 1z"/></svg>
  </div>
  <div class="abs topbar-text" style="left:194px;top:13px">(555) 014-2290</div>

  <div class="icon-dot" style="left:722px;top:12px;width:24px;height:24px">
    <svg width="12" height="10" viewBox="0 0 24 18"><path fill="#fff" d="M0 0h24v18H0z"/><path fill="none" stroke="#c4127f" stroke-width="2" d="M1 1l11 9 11-9"/></svg>
  </div>
  <div class="abs" style="left:757px;top:18px;font-size:11px;color:var(--ink)">info@brindlehoundco.com</div>
  <div class="social-dot" style="left:906px;top:11px"></div>
  <div class="social-dot" style="left:942px;top:11px"></div>
  <div class="social-dot" style="left:979px;top:11px"></div>
  <div class="social-dot" style="left:1014px;top:11px"></div>

  <nav class="nav">
    <a class="active" style="left:165px">HOME</a>
    <a style="left:232px">SERVICES</a>
    <a style="left:322px">PHOTOS</a>
    <a style="left:406px">POLICIES</a>
    <a style="left:742px">CONTACT US</a>
    <svg class="abs" style="left:851px;top:56px" width="15" height="15" viewBox="0 0 16 16"><rect x="1.5" y="3" width="13" height="11.5" rx="1" fill="none" stroke="#c4127f" stroke-width="1.5"/><path d="M1.5 6.5h13M5 1v4M11 1v4" stroke="#c4127f" stroke-width="1.5"/></svg>
    <a class="active" style="left:873px">MAKE A RESERVATION</a>
  </nav>
  <div class="underline" style="left:163px;top:79px;width:46px;height:3px"></div>
  <div class="nav-line"></div>
  <div class="brand-badge"><span>Brindle<br>Hound</span></div>
</header>

<!-- hero -->
<section class="hero">
  <div class="hero-photo" role="img" aria-label="Small fluffy cream dog standing up on its hind legs in a leafy garden"></div>
  <div class="abs hero-welcome">Welcome to</div>
  <h1 class="abs hero-title">Brindle Hound Pet<br>Boarding &amp; Daycare</h1>
  <div class="btn" style="left:163px;top:444px;width:148px;height:38px;background:var(--teal)">CONTACT US</div>
  <svg class="tear" style="top:653px" viewBox="0 0 1200 22" preserveAspectRatio="none"><use href="#torn" fill="#fff"/></svg>
</section>

<!-- about -->
<section class="about">
  <div class="about-photo" role="img" aria-label="Front of the boarding facility building under a blue sky with pine trees"></div>
  <div class="play"><svg width="20" height="22" viewBox="0 0 20 22"><path d="M4 2l14 9-14 9z" fill="#2f2f2f"/></svg></div>
  <h2 class="abs serif about-title">Who We Are</h2>
  <div class="underline" style="left:600px;top:842px;width:52px"></div>
  <div class="abs about-body">
    <p>Brindle Hound's mission is to provide gentle, loving care for your pets in a fun and friendly environment in a way that allows you, the pet owner to worry less about your companion while you are away. We want to create a stress free environment for our furry guests and a fun, playful atmosphere for our employees.</p>
    <p>A tired pup is a happy pup. That's why we have provided several indoor and outdoor play areas to stimulate your pup so he or she doesn't have time to miss you. You can rest assured your furbaby will have plenty of playful socialization throughout the day. We know how nervous pets can get when away from their humans and we want to ensure that the pet feels no anxiety during the separation.</p>
  </div>
  <div class="abs about-sign">MAREN OAKES AND DELIA FINCH, OWNERS</div>
</section>

<!-- services -->
<section class="services">
  <div class="services-band"></div>
  <svg class="tear flip" style="top:1316px" viewBox="0 0 1200 22" preserveAspectRatio="none"><use href="#torn" fill="#fff"/></svg>
  <svg class="tear" style="top:1623px" viewBox="0 0 1200 22" preserveAspectRatio="none"><use href="#torn" fill="#fff"/></svg>
  <h2 class="abs serif services-title">Our Services</h2>
  <div class="underline" style="left:578px;top:1455px;width:44px;background:var(--white)"></div>

  <div class="service-photo" style="left:180px;top:1485px;background:linear-gradient(180deg,#5e7a3e 0%,#a07a52 45%,#6f5a40 100%)" role="img" aria-label="Man playing with several dogs in a fenced yard"></div>
  <div class="service-photo" style="left:475px;top:1485px;background:linear-gradient(180deg,#d8d2c2 0%,#8aa27a 45%,#7d7060 100%)" role="img" aria-label="Indoor covered play area with dogs and play equipment"></div>
  <div class="service-photo" style="left:765px;top:1485px;background:linear-gradient(180deg,#7f8a5a 0%,#9a6a3c 45%,#c79a7c 100%)" role="img" aria-label="Small dog being held and groomed"></div>

  <div class="service-name" style="left:146px;top:1746px">Daycare</div>
  <div class="service-name" style="left:446px;top:1746px">Boarding</div>
  <div class="service-name" style="left:742px;top:1746px">Grooming</div>

  <div class="service-text" style="left:156px;top:1790px">Socialization is an important part of raising a happy and healthy pup. Brindle Hound provides daycare for your pet to alleviate loneliness and boredom...</div>
  <div class="service-text" style="left:461px;top:1790px">Brindle Hound offers overnight boarding for dogs over 6 weeks of age. We have roomy kennels for the comfort of your pet. We will provide blankets...</div>
  <div class="service-text" style="left:761px;top:1790px">Lorem ipsum dolor sit amet, nibh sed consectetuer adipiscing elit, sed diam nonummy nibeh euismod tincidunt ut laoreet dolore magna aliquam...</div>

  <div class="btn" style="left:528px;top:1923px;width:150px;height:46px">READ MORE</div>
</section>

<!-- gallery -->
<section class="gallery">
  <div class="gallery-bg"></div>
  <svg class="tear flip" style="top:2028px" viewBox="0 0 1200 22" preserveAspectRatio="none"><use href="#torn" fill="#fff"/></svg>
  <svg class="tear" style="top:2898px" viewBox="0 0 1200 22" preserveAspectRatio="none"><use href="#torn" fill="#fff"/></svg>
  <h2 class="abs serif gallery-title">Photo Gallery</h2>
  <div class="underline" style="left:578px;top:2166px;width:44px"></div>

  <div class="tile" style="left:162px;top:2202px;width:426px;height:273px;background:linear-gradient(180deg,#9c8a78 0%,#7e8a70 50%,#8a7e6e 100%)" role="img" aria-label="Several dogs playing on a dirt and grass yard"></div>
  <div class="tile" style="left:612px;top:2202px;width:426px;height:273px;background:linear-gradient(180deg,#b6a24a 0%,#8a7a3a 45%,#8aa43a 100%)" role="img" aria-label="Two small dogs sitting together in sunny grass"></div>
  <div class="tile" style="left:162px;top:2492px;width:279px;height:272px;background:linear-gradient(180deg,#9a7050 0%,#6a8a3c 55%,#5c8a30 100%)" role="img" aria-label="Black and white dog panting on grass by a wooden fence"></div>
  <div class="tile" style="left:461px;top:2492px;width:280px;height:272px;background:linear-gradient(180deg,#8a6848 0%,#7a8a44 55%,#5f8a34 100%)" role="img" aria-label="Long-haired small dogs standing on a lawn"></div>
  <div class="tile" style="left:759px;top:2492px;width:279px;height:272px;background:linear-gradient(180deg,#8a7060 0%,#d2d2cc 50%,#c8c2b4 100%)" role="img" aria-label="Dogs resting on a tiled indoor floor beside a small chair"></div>

  <div class="btn" style="left:535px;top:2801px;width:122px;height:36px;font-size:13px">VIEW ALL</div>
</section>

<!-- contact -->
<section class="contact">
  <h2 class="abs serif contact-title">Contact Us</h2>
  <div class="underline" style="left:578px;top:3052px;width:44px"></div>

  <div class="c-icon" style="top:3114px">
    <svg width="22" height="28" viewBox="0 0 22 28"><path d="M11 26s9-9.5 9-15.5a9 9 0 0 0-18 0C2 16.5 11 26 11 26z" fill="none" stroke="#c4127f" stroke-width="2"/><circle cx="11" cy="10.5" r="3.5" fill="none" stroke="#c4127f" stroke-width="2"/></svg>
  </div>
  <div class="c-label" style="top:3110px">Brindle Hound</div>
  <div class="c-val" style="top:3135px">480 Cedar Mill Road Marlow,<br>GA&nbsp; 31599</div>

  <div class="c-icon" style="top:3213px">
    <svg width="28" height="20" viewBox="0 0 28 20"><rect x="1" y="1" width="26" height="18" rx="2" fill="none" stroke="#c4127f" stroke-width="2"/><path d="M1 2l13 10 13-10" fill="none" stroke="#c4127f" stroke-width="2"/></svg>
  </div>
  <div class="c-label" style="top:3219px">Email:</div>
  <div class="c-val" style="top:3245px">info@brindlehoundco.com</div>

  <div class="c-icon" style="top:3309px">
    <svg width="24" height="24" viewBox="0 0 24 24"><path fill="none" stroke="#c4127f" stroke-width="1.8" d="M6.6 10.8a15 15 0 0 0 6.6 6.6l2.2-2.2a1 1 0 0 1 1-.25 11.4 11.4 0 0 0 3.6.57 1 1 0 0 1 1 1V20a1 1 0 0 1-1 1A17 17 0 0 1 3 4a1 1 0 0 1 1-1h3.5a1 1 0 0 1 1 1c0 1.25.2 2.45.57 3.57a1 1 0 0 1-.25 1z"/></svg>
  </div>
  <div class="c-label" style="left:276px;top:3316px">Phone:</div>
  <div class="c-val" style="left:276px;top:3340px;font-size:19px;line-height:26px">(555) 014-2290</div>

  <div class="c-icon" style="top:3407px">
    <svg width="28" height="28" viewBox="0 0 28 28"><circle cx="14" cy="14" r="12" fill="none" stroke="#c4127f" stroke-width="2"/><circle cx="14" cy="14" r="8" fill="none" stroke="#c4127f" stroke-width="1.5"/><path d="M14 9v5h4" fill="none" stroke="#c4127f" stroke-width="2"/></svg>
  </div>
  <div class="c-val" style="top:3417px;font-weight:500;line-height:20px">Mon – Sat 7:30am–6:00pm<br>Sunday Boarding Pick Up/ Drop off<br>By Appointment</div>

  <div class="form-box">
    <h3>Send Us A Message</h3>
    <div class="rule"></div>
    <div class="field" style="top:92px;height:36px">Name*</div>
    <div class="field" style="top:140px;height:36px">Email*</div>
    <div class="field" style="top:189px;height:36px">Phone*</div>
    <div class="field" style="top:238px;height:60px">How can we help today?*</div>
    <div class="btn" style="left:37px;top:314px;width:112px;height:34px;font-size:13px">SEND</div>
  </div>
</section>

<!-- footer -->
<footer>
  <div class="footer"></div>
  <svg class="tear flip" style="top:3566px" viewBox="0 0 1200 22" preserveAspectRatio="none"><use href="#torn" fill="#3a3a3a"/></svg>
  <div class="abs footer-brand">Brindle Hound</div>
  <div class="footer-line" style="top:3802px"></div>
  <nav class="footer-nav">
    <a style="left:290px">HOME</a>
    <a style="left:395px">SERVICES</a>
    <a style="left:523px">PHOTOS</a>
    <a style="left:645px">POLICIES</a>
    <a style="left:770px">CONTACT US</a>
  </nav>
  <div class="footer-line" style="top:3862px"></div>
  <div class="abs copy">Copyright © 2020 Brindle Hound. All Rights Reserved.</div>
  <div class="f-social" style="left:907px"></div>
  <div class="f-social" style="left:942px"></div>
  <div class="f-social" style="left:976px"></div>
  <div class="f-social" style="left:1011px"></div>
</footer>

</body>
</html>
```